Real State Agency App

We need an app design for a real state agency, we provide mockups for our project that ilustrates very well what we need
our web site is www.brightkeyhomes-example.com,

Target Market(s)

Tourism

Font styles to use
Other font styles liked:
• attached you will find it

Requirements
Must have
• Colors like the logo

```html
<!DOCTYPE html>
<html lang="en">
<head>
<meta charset="utf-8">
<title>Brightkey – Real Estate App Screens</title>
<link href="https://fonts.googleapis.com/css2?family=Raleway:wght@400;500;600&display=swap" rel="stylesheet">
<style>
  :root {
    --stage: #c9c9c9;
    --screen: #10223a;
    --ink: #ffffff;
    --ink-soft: #c9d2de;
    --line: #aeb8c6;
    --brand: #3b6fd1;
    --brand-gold: #e3a21c;
    --list-bg: #e2e2e2;
    --list-ink: #2a2a2a;
    --link: #2f6fd6;
    --accent-red: #d62a2a;
  }
  * { box-sizing: border-box; margin: 0; padding: 0; }
  html, body { width: 1200px; height: 1200px; overflow: hidden; }
  body { background: var(--stage); font-family: "Raleway", sans-serif; color: var(--ink); position: relative; }

  .screen {
    position: absolute; width: 200px; height: 432px;
    background: var(--screen); border-radius: 28px; overflow: hidden;
  }
  .screen--home { left: 60px; top: 78px; }
  .screen--sell { left: 488px; top: 78px; }
  .screen--search { left: 943px; top: 78px; }
  .screen--contact { left: 60px; top: 620px; }
  .screen--services { left: 354px; top: 620px; }
  .screen--results { left: 649px; top: 620px; }
  .screen--detail { left: 943px; top: 620px; }

  .abs { position: absolute; }
  .nav-home { left: 20px; top: 28px; width: 18px; height: 16px; }
  .nav-right { right: 20px; top: 28px; width: 16px; height: 16px; }

  .hero-icon { left: 50%; transform: translateX(-50%); top: 66px; width: 40px; height: 40px; }
  .screen-title { left: 0; right: 0; top: 120px; text-align: center; font-size: 11.5px; font-weight: 500; }
  .body-text { left: 33px; width: 134px; font-size: 6.6px; line-height: 1.3; text-align: justify; }

  .field {
    position: absolute; left: 64px; width: 72px; height: 12px;
    border: 1px solid var(--line); border-radius: 2px;
    font-size: 4.2px; color: var(--ink-soft); padding: 2.5px 3px;
  }
  .field--select::after { content: "⌄"; position: absolute; right: 2px; top: -1px; font-size: 6px; }
  .field--area { height: 31px; }
  .btn {
    position: absolute; border: 1px solid var(--line); border-radius: 2px;
    font-size: 5.6px; display: flex; align-items: center; justify-content: center;
    color: var(--ink); box-shadow: 0 1px 2px rgba(0,0,0,.5);
  }

  /* home */
  .brand { left: 0; right: 0; top: 58px; text-align: center; font-size: 20px; font-weight: 500; color: var(--brand); letter-spacing: 1px; }
  .menu-btn {
    position: absolute; left: 32px; width: 136px; height: 42px;
    border: 1.5px solid var(--line); border-radius: 2px;
    display: flex; align-items: center; padding-left: 12px; gap: 8px;
    font-size: 7px; font-weight: 500;
  }
  .menu-btn svg { width: 20px; height: 20px; flex: none; }
  .languages { left: 0; right: 0; top: 412px; text-align: center; font-size: 7px; }
  .languages u { text-underline-offset: 1px; }

  /* services */
  .service-btn { left: 63px; width: 73px; height: 22px; font-size: 5px; }

  /* results */
  .results-head { left: 0; right: 0; top: 52px; text-align: center; font-size: 7px; }
  .results-query { left: 0; right: 0; top: 67px; text-align: center; font-size: 6.5px; color: var(--ink-soft); }
  .results-query b { color: var(--ink); font-weight: 500; }
  .results-list { left: 15px; top: 93px; width: 170px; height: 305px; background: var(--list-bg); display: flex; flex-direction: column; }
  .result { flex: 1; display: flex; align-items: center; gap: 4px; padding: 2px 0; border-bottom: 1px solid #c4c4c4; }
  .result--flip { flex-direction: row-reverse; }
  .result-photo { width: 105px; height: 66px; flex: none; border-radius: 1px; }
  .photo-a { background: linear-gradient(180deg, #8fb4d6 0%, #e8e8e6 55%, #3fa7b8 80%, #5c8a3a 100%); }
  .photo-b { background: linear-gradient(180deg, #6d96c4 0%, #b7c3cf 45%, #2b4a6b 75%, #3c6a88 100%); }
  .photo-c { background: linear-gradient(180deg, #7ea9d3 0%, #ddd8cf 50%, #36b1c8 80%, #8a6a4a 100%); }
  .photo-d { background: linear-gradient(180deg, #5f9bd0 0%, #8b5a3c 45%, #2fa59e 75%, #5a7a3a 100%); }
  .result-text { font-size: 4.4px; line-height: 1.35; color: var(--list-ink); padding: 0 3px; }
  .result-text .red { color: var(--accent-red); }
  .result-text a { color: var(--link); }
  .pager { left: 15px; right: 15px; top: 414px; display: flex; justify-content: space-between; font-size: 4.5px; color: var(--ink-soft); }

  /* detail */
  .detail-photo { left: 15px; top: 61px; width: 170px; height: 113px; border: 1px solid #6a7789;
    background: linear-gradient(180deg, #5a6d82 0%, #c9b08a 45%, #2c3a48 65%, #1f5f7a 80%, #3d6a35 100%); }
  .detail-title { left: 0; right: 0; top: 187px; text-align: center; font-size: 11px; font-weight: 500; }
  .detail-text { left: 41px; width: 118px; font-size: 6.4px; line-height: 1.3; text-align: justify; }
</style>
</head>
<body>

<svg width="0" height="0" style="position:absolute">
  <defs>
    <symbol id="i-house" viewBox="0 0 24 22"><path d="M12 1 1 11h3v10h6v-6h4v6h6V11h3z" fill="currentColor"/></symbol>
    <symbol id="i-search" viewBox="0 0 24 24"><circle cx="10" cy="10" r="7" fill="none" stroke="currentColor" stroke-width="2"/><path d="M15 15l7 7" stroke="currentColor" stroke-width="2" stroke-linecap="round"/></symbol>
    <symbol id="i-search-bold" viewBox="0 0 24 24"><circle cx="10" cy="10" r="6.5" fill="none" stroke="currentColor" stroke-width="3.5"/><path d="M15 15l6 6" stroke="currentColor" stroke-width="4" stroke-linecap="round"/></symbol>
    <symbol id="i-phone" viewBox="0 0 24 24"><path d="M6 2c1 0 2 3 3 5 .4 1-1 2-1.5 3 1 2.5 3 4.5 5.5 5.5 1-.5 2-2 3-1.5 2 1 5 2 5 3s-2 4-4 4C9 21 3 14 2 7c0-2 3-5 4-5z" fill="currentColor"/></symbol>
    <symbol id="i-phone-line" viewBox="0 0 24 24"><path d="M6 2c1 0 2 3 3 5 .4 1-1 2-1.5 3 1 2.5 3 4.5 5.5 5.5 1-.5 2-2 3-1.5 2 1 5 2 5 3s-2 4-4 4C9 21 3 14 2 7c0-2 3-5 4-5z" fill="none" stroke="currentColor" stroke-width="1"/></symbol>
    <symbol id="i-info" viewBox="0 0 12 24"><circle cx="6" cy="3" r="2.6" fill="currentColor"/><path d="M2 8h6v12h2.5v3h-9v-3H4v-9H2z" fill="currentColor"/></symbol>
    <symbol id="i-info-line" viewBox="0 0 24 24"><circle cx="12" cy="4" r="2" fill="none" stroke="currentColor"/><path d="M9.5 9h4v11h2v2h-6v-2h1.5v-9h-1.5z" fill="none" stroke="currentColor"/></symbol>
    <symbol id="i-house-line" viewBox="0 0 24 24"><path d="M12 3 2 12h3v9h5v-6h4v6h5v-9h3z" fill="none" stroke="currentColor"/></symbol>
    <symbol id="i-list" viewBox="0 0 24 20"><g fill="currentColor"><rect x="0" y="1" width="3" height="3"/><rect x="0" y="8.5" width="3" height="3"/><rect x="0" y="16" width="3" height="3"/><rect x="6" y="1.5" width="18" height="2"/><rect x="6" y="9" width="18" height="2"/><rect x="6" y="16.5" width="18" height="2"/></g></symbol>
  </defs>
</svg>

<!-- Home menu -->
<section class="screen screen--home">
  <div class="abs brand">Brightkey</div>
  <div class="menu-btn" style="top:111px"><svg style="color:var(--line)"><use href="#i-search"/></svg>Serach Our Properties</div>
  <div class="menu-btn" style="top:168px"><svg style="color:var(--line)"><use href="#i-info-line"/></svg>Our Services</div>
  <div class="menu-btn" style="top:224px"><svg style="color:var(--line)"><use href="#i-house-line"/></svg>Sell your Property with us</div>
  <div class="menu-btn" style="top:279px;padding-left:38px"><svg style="color:var(--line)"><use href="#i-phone-line"/></svg>Contact</div>
  <div class="abs languages">Spain | <u>English</u> | German</div>
</section>

<!-- Sell property -->
<section class="screen screen--sell">
  <svg class="abs nav-home"><use href="#i-house"/></svg>
  <svg class="abs nav-right"><use href="#i-search"/></svg>
  <svg class="abs hero-icon"><use href="#i-house"/></svg>
  <div class="abs screen-title">Sell Property with us</div>
  <p class="abs body-text" style="top:166px">Cuando usted esta considerando la posibilidad de vender su propiedad, siempre puede trater de venderla usted mismo o puede hacerlo a traves de una inmobiliaria profesional, cosmo somos Brightkey.</p>
  <div class="field" style="top:229px">Name</div>
  <div class="field" style="top:246px">Surname</div>
  <div class="field" style="top:263px">Phone</div>
  <div class="field" style="top:280px">Email</div>
  <div class="field" style="top:297px">Property Name</div>
  <div class="field field--select field--area" style="top:314px">Property Description</div>
  <div class="btn" style="left:64px;top:373px;width:72px;height:22px">Send us your property</div>
</section>

<!-- Search -->
<section class="screen screen--search">
  <svg class="abs nav-home"><use href="#i-house"/></svg>
  <svg class="abs hero-icon"><use href="#i-search-bold"/></svg>
  <div class="abs screen-title">Search Properties</div>
  <div class="field field--select" style="top:152px">To Reform</div>
  <div class="field" style="top:169px">Key</div>
  <div class="field field--select" style="top:186px">Type</div>
  <div class="field field--select" style="top:203px">Area</div>
  <div class="btn" style="left:63px;top:231px;width:74px;height:21px">Search Properties</div>
</section>

<!-- Contact -->
<section class="screen screen--contact">
  <svg class="abs nav-home"><use href="#i-house"/></svg>
  <svg class="abs nav-right"><use href="#i-search"/></svg>
  <svg class="abs hero-icon"><use href="#i-phone"/></svg>
  <div class="abs screen-title">Contact us</div>
  <div class="field" style="top:159px">Name</div>
  <div class="field" style="top:176px">Surname</div>
  <div class="field" style="top:193px">Phone</div>
  <div class="field" style="top:210px">Email</div>
  <div class="field field--select" style="top:227px">Property Name</div>
  <div class="field field--select field--area" style="top:244px">Notes</div>
  <div class="btn" style="left:63px;top:303px;width:74px;height:22px">Send us your message</div>
</section>

<!-- Services -->
<section class="screen screen--services">
  <svg class="abs nav-home"><use href="#i-house"/></svg>
  <svg class="abs nav-right"><use href="#i-search"/></svg>
  <svg class="abs hero-icon" style="width:20px"><use href="#i-info"/></svg>
  <div class="abs screen-title">Our Services</div>
  <p class="abs body-text" style="top:157px">Cala d' Or es un sitio emblematico de la costa del levante mallorquin. Esta zona costera y sus alrededores son uno de los primeros lugares turisticos de Mallorca y se encuentran a tan solo 45 minutos del aeropuerto y de la fabulosa capital de Palma.</p>
  <div class="btn service-btn" style="top:246px">SEGUROS</div>
  <div class="btn service-btn" style="top:277px">COMPRA</div>
  <div class="btn service-btn" style="top:307px">MANTENIMIENTOS</div>
  <div class="btn service-btn" style="top:338px">OBRAS Y REFORMAS</div>
</section>

<!-- Results -->
<section class="screen screen--results">
  <svg class="abs nav-home"><use href="#i-house"/></svg>
  <svg class="abs nav-right"><use href="#i-search"/></svg>
  <div class="abs results-head">Search results for</div>
  <div class="abs results-query">Key: <b>Beach,</b> &nbsp; Type: <b>House,</b> &nbsp; Area: <b>Palma</b></div>
  <div class="abs results-list">
    <div class="result">
      <div class="result-photo photo-a" role="img" aria-label="Photo of a modern white villa with a pool"></div>
      <p class="result-text">A paragraph of <span class="red">text</span> with an <a>unassigned link</a>. A second row of text with a <a>web link</a>.</p>
    </div>
    <div class="result result--flip">
      <div class="result-photo photo-b" role="img" aria-label="Photo of a modern villa at dusk with a pool"></div>
      <p class="result-text">A paragraph of <span class="red">text</span> with an <a>unassigned link</a>. A second row of text with a <a>web link</a>.</p>
    </div>
    <div class="result">
      <div class="result-photo photo-c" role="img" aria-label="Photo of a villa with a wooden deck and pool"></div>
      <p class="result-text">A paragraph of <span class="red">text</span> with an <a>unassigned link</a>. A second row of text with a <a>web link</a>.</p>
    </div>
    <div class="result result--flip">
      <div class="result-photo photo-d" role="img" aria-label="Photo of a tropical house with a turquoise pool"></div>
      <p class="result-text">A paragraph of <span class="red">text</span> with an <a>unassigned link</a>. A second row of text with a <a>web link</a>.</p>
    </div>
  </div>
  <div class="abs pager"><span>‹ Previous Page</span><span>Next Page ›</span></div>
</section>

<!-- Property detail -->
<section class="screen screen--detail">
  <svg class="abs nav-home"><use href="#i-house"/></svg>
  <svg class="abs nav-right" style="width:18px"><use href="#i-list"/></svg>
  <div class="abs detail-photo" role="img" aria-label="Photo of a modern villa lit at dusk with a pool and lawn"></div>
  <div class="abs detail-title">Villa Brightkey</div>
  <p class="abs detail-text" style="top:207px">Rustic historical farmhouse on top of a hill outside of Sineu within a protected area full of mediterranean oak trees, pine trees etc.</p>
  <p class="abs detail-text" style="top:261px">3 bedrooms | bathroom | large equipped kitchen with granit and marble worktop and an antic bread oven | big living room with fireplace | pool | terraces | option to construc 2-3 bedrooms | all licences in older | natural stone house</p>
  <div class="btn" style="left:60px;top:350px;width:80px;height:21px">Send Request Information</div>
</section>

</body>
</html>
```